Venue Booking Site

I would like a venue directory and booking website designed. The idea is that end users will come to the site to find venues for weddings, parties, events etc. They will be able to find the venue based on many criteria, the most important ones are availability and location - they will be able to see in real time which venues are available for the desired dates and areas.

Venues will be able to use the website as a reservation management tool, receive payments for bookings through the site and be able to manage bookings on the go. This will be made into an app. It needs to be developed in bootstrap. Brand name to be used: Pinevault. Venue, place and space bookings.

Target audience - end users - anyone who is looking for a venue. For Community members it will provide an easy way to find a suitable venue
Outline what dates and times the venue is available
Outline costs involved in booking the venue
Search via many other criteria
It will allow the customer to book and pay for the venue online in one smooth process

Clients: Venue managers - particularly focussing on not for profit businesses eg, GPWs, community hall managers, small business managers. These people typically use paper based systems yet and do not use websites so it needs to be very user friendly. Future growth to restaurants, pubs, event venues who have a stronger familiarity with computers and who might already use their own booking management tool - so this needs to be able to link in with their system.

What need will this meet for venue managers:
This tool provides venues with greater visibility, promotion and advertising of their venue
This allows more customers to find them and book with them
This tool will be offered to not-for-profit venue managers for free to better connect them to the community
This means greater profit for these community venues
This means more revenue and jobs created in these communities

Sample of the layout / contents attached. This is not a complete site map as yet as it is a work in progress for final pages.

Industry/Entity Type

Small Business

Number of Pages Required

5+ page

Font styles to use
Sans Serif

Colors
eb2027

Requirements
Must have
• This is a psd file only - one template for each different section, home page, search page, detailed page view, admin back end
Should not have
• does not need to be coded.
• Note, the lantern quay logo jpeg files were files we were toying with using for this project- but I am happy to use the main pinevault logo- I will let you decide.

```html
<!DOCTYPE html>
<html lang="en">
<head>
<meta charset="utf-8">
<title>Pinevault – Venue, place and space bookings</title>
<link rel="stylesheet" href="https://fonts.googleapis.com/css2?family=Open+Sans:wght@400;600;700&family=Signika:wght@400;600&display=swap">
<style>
:root{
  --red:#eb2027;
  --red-soft:#f04a4a;
  --dark:#231f20;
  --orange:#f7a21b;
  --peach:#fdd8a6;
  --coral:#f36a4c;
  --white:#ffffff;
  --grey-line:#d6d6d6;
  --text:#4a4a4a;
  --muted:#8a8a8a;
  --star:#f2a623;
}
*{box-sizing:border-box;margin:0;padding:0}
html,body{width:720px;height:1200px;overflow:hidden}
body{position:relative;font-family:"Open Sans",Arial,sans-serif;color:var(--text);background:var(--dark)}
.abs{position:absolute}

/* top bar */
.topbar{left:0;top:0;width:720px;height:19px;background:var(--red);color:var(--white);font-size:11px;font-weight:700}
.topbar .support{left:113px;top:2px;display:flex;align-items:center;gap:6px}
.topbar .account{left:522px;top:2px;display:flex;align-items:center;gap:8px;font-weight:600;font-size:10px}

/* header */
.header{left:0;top:19px;width:720px;height:77px;background:var(--dark)}
.logo{left:111px;top:14px;display:flex;align-items:center;gap:8px}
.logo .mark{width:20px;height:20px;background:var(--red)}
.logo .name{font-size:27px;font-weight:700;color:var(--white);letter-spacing:-.5px}
.site-search{left:410px;top:10px;width:130px;height:19px;background:var(--white);border-radius:2px;font-size:8px;color:var(--muted);padding:4px 6px;white-space:nowrap}
.site-search svg{position:absolute;right:5px;top:4px}
.list-venue{left:545px;top:10px;width:67px;height:19px;background:var(--orange);border-radius:2px;color:var(--dark);font-size:8px;font-weight:600;text-align:center;line-height:19px;white-space:nowrap}
.nav{left:296px;top:43px;display:flex;gap:2px;font-size:8.5px;font-weight:600;color:var(--white);white-space:nowrap}
.nav a{color:var(--white);text-decoration:none;padding:4px 5px}
.nav a.active{background:var(--red);border-radius:2px}
.header-notch{left:574px;top:94px}

/* hero */
.hero{left:0;top:96px;width:720px;height:411px;background:linear-gradient(180deg,var(--peach) 0%,#f9a877 30%,var(--coral) 60%,var(--red-soft) 100%)}
.slider{left:117px;top:25px;width:487px;height:221px;background:var(--white);box-shadow:0 4px 10px rgba(0,0,0,.25)}
.photo{position:absolute}
.ph-tower{left:7px;top:7px;width:119px;height:207px;background:linear-gradient(180deg,#5d6f8a,#2f3440 70%,#6b5a3c)}
.ph-room{left:129px;top:7px;width:216px;height:106px;background:linear-gradient(135deg,#b9854a,#6a3f20 60%,#e7d3b0)}
.ph-resort{left:129px;top:116px;width:106px;height:98px;background:linear-gradient(180deg,#7fb5dc,#3f8f6a 55%,#2c9bc4)}
.ph-lobby{left:238px;top:116px;width:107px;height:98px;background:linear-gradient(180deg,#2b1f14,#c18a3c 60%,#5b3a1e)}
.slide-panel{left:353px;top:0;width:134px;height:221px;background:var(--dark);color:var(--white);padding:12px 9px}
.slide-panel h2{font-family:Arial,"Open Sans",sans-serif;font-size:16px;font-weight:400;line-height:1.25;letter-spacing:.3px}
.slide-panel p{margin-top:10px;font-size:8.5px;line-height:1.45}
.dots{left:63px;top:196px;display:flex;gap:5px}
.dots i{width:5px;height:5px;border-radius:50%;background:#6b6b6b;display:block}
.dots i.on{background:var(--red)}

/* search form */
.finder{left:0;top:284px;width:720px;height:130px}
.finder h3{position:absolute;font-family:"Signika",sans-serif;font-weight:600;font-size:13px;color:var(--white);text-shadow:0 1px 2px rgba(0,0,0,.35)}
.finder .col-line{position:absolute;top:6px;width:1px;height:72px;background:rgba(255,255,255,.35)}
.finder label{position:absolute;font-size:8px;color:var(--white);white-space:nowrap}
.radio-list{position:absolute;left:145px;top:25px;list-style:none;font-size:8px;color:var(--white)}
.radio-list li{display:flex;align-items:center;gap:5px;height:14px;white-space:nowrap}
.radio-list i{width:8px;height:8px;border-radius:50%;background:var(--white);display:block}
.radio-list i.on{box-shadow:inset 0 0 0 2px var(--white);background:#2e7d32}
.field{position:absolute;height:18px;background:var(--white);border:1px solid #ccc;border-radius:2px;font-size:7.5px;line-height:9px;color:var(--muted);padding:4px 14px 4px 5px;white-space:nowrap;overflow:hidden}
.field.plain{padding-right:5px}
.field svg{position:absolute;right:3px;top:4px}
.btn-search{position:absolute;left:331px;top:91px;width:58px;height:20px;background:linear-gradient(180deg,#fcc04a,var(--orange));border-radius:2px;color:var(--dark);font-size:9px;font-weight:700;text-align:center;line-height:20px}

/* top venues */
.venues{left:111px;top:509px;width:499px;height:297px;background:var(--white);border-radius:8px;overflow:hidden}
.section-head{height:36px;background:linear-gradient(180deg,#fde0b1,#fbc68f);text-align:center;font-family:"Signika",sans-serif;font-size:16px;color:var(--dark);line-height:36px}
.venue{position:absolute;width:234px;height:108px;background:#ececec;border-radius:3px;padding:5px}
.venue .pic{position:absolute;left:5px;top:5px;width:112px;height:98px}
.venue .pic span{position:absolute;left:0;bottom:0;width:100%;height:14px;background:rgba(0,0,0,.75);color:var(--white);font-size:8px;font-weight:700;line-height:14px;padding-left:7px;letter-spacing:.2px;white-space:nowrap}
.venue .info{position:absolute;left:123px;top:5px;width:105px}
.venue .title{display:flex;justify-content:space-between;font-size:8.5px;color:#555;border-bottom:1px solid var(--grey-line);padding-bottom:3px}
.venue .desc{font-size:7px;line-height:1.35;color:var(--muted);margin-top:4px}
.venue .rate{display:flex;justify-content:space-between;align-items:center;margin-top:4px;font-size:7px;color:var(--red)}
.venue .stars{display:flex;gap:1px}
.venue .per{font-size:7px;color:#555;margin-top:3px;white-space:nowrap}
.venue .buy{display:flex;justify-content:space-between;align-items:center;margin-top:2px}
.venue .price{font-size:11px;font-weight:700;color:var(--red)}
.venue .book{background:var(--red);color:var(--white);font-size:8px;font-weight:600;padding:3px 7px;border-radius:2px}
.pic-patio{background:linear-gradient(180deg,#6d8fae,#c8b08c 55%,#3b332c)}
.pic-pool{background:linear-gradient(180deg,#102534,#2aa3c7 55%,#e6c06b)}
.pic-garden{background:linear-gradient(180deg,#6a86a8,#8a6a3f 50%,#2f3b22)}
.pic-villa{background:linear-gradient(180deg,#3a5f93,#b7c7d6 55%,#4f4a3c)}

/* why */
.why{left:111px;top:827px;width:499px;height:224px;background:var(--white);border-radius:8px}
.why h2{text-align:center;font-family:"Signika",sans-serif;font-weight:400;font-size:16px;color:var(--dark);margin-top:10px}
.why h2 em{font-style:normal;color:var(--red)}
.reason{position:absolute;width:110px;font-size:7px;line-height:1.4;color:var(--muted);text-align:justify}
.reason h4{font-family:"Signika",sans-serif;font-weight:400;font-size:9px;color:var(--red);text-align:left;padding-bottom:4px;border-bottom:1px solid var(--grey-line);margin-bottom:4px;white-space:nowrap}
.reason-line{position:absolute;width:1px;height:62px;background:var(--grey-line)}

/* footer */
.footer{left:0;top:1077px;width:720px;height:123px;background:linear-gradient(180deg,#f8f8f8,#e9e9e9)}
.foot-brand{left:105px;top:22px;display:flex;align-items:center;gap:6px;font-size:9px;font-weight:700;color:var(--dark)}
.foot-brand .mark{width:10px;height:10px;background:var(--red)}
.contact{left:107px;top:45px;list-style:none;font-size:7.5px;color:#555}
.contact li{display:flex;align-items:center;gap:6px;height:13px;white-space:nowrap}
.foot-col{font-size:9px;font-weight:700;color:var(--dark)}
.support-list{left:235px;top:43px;list-style:none;font-size:7.5px;color:#555}
.support-list li{height:12px;white-space:nowrap}
.social{left:367px;top:40px;display:flex;gap:5px}
.social i{width:14px;height:14px;border-radius:50%;background:#4b4b4b;display:block}
.social i.on{background:#3b5a9a}
.offers{left:367px;top:67px;display:flex;align-items:center;gap:5px;font-size:8px;font-weight:700;color:var(--dark);white-space:nowrap}
.offers .email{width:104px;height:14px;background:var(--white);border:1px solid #ccc;font-size:6.5px;font-weight:400;color:var(--muted);padding:2px 4px}
.offers .signup{background:var(--red);color:var(--white);font-size:7px;padding:3px 5px}
.foot-nav{left:0;top:104px;width:720px;height:19px;border-top:1px solid var(--grey-line)}
.foot-nav ul{position:absolute;left:111px;top:4px;display:flex;list-style:none;font-size:7px;color:#555;white-space:nowrap}
.foot-nav li{padding:0 6px;border-right:1px solid #bbb}
.foot-nav li:first-child{padding-left:4px}
.foot-nav li:last-child{border-right:none}
.copyright{position:absolute;left:472px;top:5px;font-size:7px;color:#555;white-space:nowrap}
</style>
</head>
<body>

<div class="abs topbar">
  <div class="abs support">
    <svg width="11" height="11" viewBox="0 0 12 12"><circle cx="6" cy="6" r="6" fill="#fff"/><path d="M3.6 3.2l1.3-.3.7 1.5-.8.6c.4.9 1 1.5 1.9 1.9l.6-.8 1.5.7-.3 1.3C6 8.3 3.7 6 3.6 3.2z" fill="#eb2027"/></svg>
    <span>24/7 Support&nbsp;&nbsp;&nbsp;03 5550 1427</span>
  </div>
  <div class="abs account">
    <svg width="11" height="11" viewBox="0 0 12 12"><rect x="1" y="2" width="10" height="9" fill="none" stroke="#fff" stroke-width="1.2"/><path d="M1 5h10M4 1v2M8 1v2" stroke="#fff" stroke-width="1.2"/></svg>
    <span>Login | Sign Up</span>
  </div>
</div>

<header class="abs header">
  <div class="abs logo"><span class="mark"></span><span class="name">pinevault</span></div>
  <div class="abs site-search">Search entire Site here
    <svg width="9" height="9" viewBox="0 0 10 10"><circle cx="4" cy="4" r="3" fill="none" stroke="#777" stroke-width="1.3"/><path d="M6.3 6.3L9 9" stroke="#777" stroke-width="1.4"/></svg>
  </div>
  <div class="abs list-venue">List My Venue</div>
  <nav class="abs nav">
    <a class="active">HOME</a><a>VENUE</a><a>NEWS &amp; OFFERS</a><a>INSPIRATION</a><a>SERVICES</a><a>CONTACT</a><a>FAQs</a>
  </nav>
</header>

<section class="abs hero">
  <div class="abs slider">
    <div class="photo ph-tower" role="img" aria-label="Photo of a modern glass hotel tower at dusk"></div>
    <div class="photo ph-room" role="img" aria-label="Photo of a hotel bedroom with a large bed"></div>
    <div class="photo ph-resort" role="img" aria-label="Photo of a beach resort with pool and palm trees"></div>
    <div class="photo ph-lobby" role="img" aria-label="Photo of a grand hotel lobby with a statue"></div>
    <div class="abs slide-panel">
      <h2>LOREM IPSUM DOLOR SIT AMET, CONSE CTETUER.</h2>
      <p>LOREM IPSUM DOLOR SIT AMET, CONSE CTETUER AMET, CONSE CTETUER.</p>
      <div class="abs dots"><i class="on"></i><i></i><i></i><i></i></div>
    </div>
  </div>

  <form class="abs finder">
    <h3 style="left:149px;top:0">What?</h3>
    <ul class="radio-list">
      <li><i class="on"></i>Hotel</li><li><i></i>Rent a Car</li><li><i></i>Self Catering</li><li><i></i>Tour</li>
    </ul>
    <span class="col-line" style="left:219px"></span>

    <h3 style="left:271px;top:0">Where</h3>
    <label style="left:229px;top:25px">Your Desination</label>
    <div class="field plain" style="left:229px;top:38px;width:120px">City, Region, District or specific</div>
    <span class="col-line" style="left:361px"></span>

    <h3 style="left:407px;top:0">When?</h3>
    <label style="left:372px;top:25px">Check in Date</label>
    <label style="left:434px;top:25px">Check-out Date</label>
    <div class="field" style="left:372px;top:38px;width:58px">13/12/2014
      <svg width="9" height="9" viewBox="0 0 10 10"><rect x="1" y="2" width="8" height="7" fill="none" stroke="#888"/><path d="M1 4.5h8" stroke="#888"/></svg></div>
    <div class="field" style="left:434px;top:38px;width:58px">15/12/2014
      <svg width="9" height="9" viewBox="0 0 10 10"><rect x="1" y="2" width="8" height="7" fill="none" stroke="#888"/><path d="M1 4.5h8" stroke="#888"/></svg></div>
    <span class="col-line" style="left:505px"></span>

    <h3 style="left:541px;top:0">Who?</h3>
    <label style="left:518px;top:25px">Rooms</label>
    <div class="field" style="left:518px;top:38px;width:55px">2 Rooms
      <svg width="8" height="10" viewBox="0 0 8 10"><path d="M1 4l3-3 3 3M1 6l3 3 3-3" fill="none" stroke="#777"/></svg></div>

    <div class="btn-search">SEARCH</div>
  </form>
</section>

<svg class="abs header-notch" width="18" height="14" viewBox="0 0 18 14"><path d="M0 0h18L4 14z" fill="#231f20"/></svg>

<section class="abs venues">
  <div class="section-head">Our Top Venues</div>

  <article class="venue" style="left:9px;top:46px">
    <div class="pic pic-patio" role="img" aria-label="Photo of a modern apartment patio with lounge chairs"><span>PRIME APPARTMENT</span></div>
    <div class="info">
      <div class="title"><span>Ut wisi enim</span><span>8/10</span></div>
      <p class="desc">Lorem ipsum dolor sit amet, consectetuer adipiscing elit, sed diam nonummy nibh euismod.</p>
      <div class="rate"><span class="stars"><svg width="40" height="7" viewBox="0 0 40 7"><g fill="#f2a623"><circle cx="3.5" cy="3.5" r="3"/><circle cx="11.5" cy="3.5" r="3"/><circle cx="19.5" cy="3.5" r="3"/></g><g fill="#ccc"><circle cx="27.5" cy="3.5" r="3"/><circle cx="35.5" cy="3.5" r="3"/></g></svg></span><span>More Info</span></div>
      <p class="per">Price per room per night from</p>
      <div class="buy"><span class="price">$80</span><span class="book">Book Now</span></div>
    </div>
  </article>

  <article class="venue" style="left:256px;top:46px">
    <div class="pic pic-pool" role="img" aria-label="Photo of a resort pool lit at night"><span>SUNSET LAGOON</span></div>
    <div class="info">
      <div class="title"><span>Ut wisi enim</span><span>8/10</span></div>
      <p class="desc">Lorem ipsum dolor sit amet, consectetuer adipiscing elit, sed diam nonummy nibh euismod.</p>
      <div class="rate"><span class="stars"><svg width="40" height="7" viewBox="0 0 40 7"><g fill="#f2a623"><circle cx="3.5" cy="3.5" r="3"/><circle cx="11.5" cy="3.5" r="3"/><circle cx="19.5" cy="3.5" r="3"/></g><g fill="#ccc"><circle cx="27.5" cy="3.5" r="3"/><circle cx="35.5" cy="3.5" r="3"/></g></svg></span><span>More Info</span></div>
      <p class="per">Price per room per night from</p>
      <div class="buy"><span class="price">$80</span><span class="book">Book Now</span></div>
    </div>
  </article>

  <article class="venue" style="left:9px;top:170px">
    <div class="pic pic-garden" role="img" aria-label="Photo of a villa garden path at dusk"><span>VILLA IPSUM</span></div>
    <div class="info">
      <div class="title"><span>Ut wisi enim</span><span>8/10</span></div>
      <p class="desc">Lorem ipsum dolor sit amet, consectetuer adipiscing elit, sed diam nonummy nibh euismod.</p>
      <div class="rate"><span class="stars"><svg width="40" height="7" viewBox="0 0 40 7"><g fill="#f2a623"><circle cx="3.5" cy="3.5" r="3"/><circle cx="11.5" cy="3.5" r="3"/><circle cx="19.5" cy="3.5" r="3"/></g><g fill="#ccc"><circle cx="27.5" cy="3.5" r="3"/><circle cx="35.5" cy="3.5" r="3"/></g></svg></span><span>More Info</span></div>
      <p class="per">Price per room per night from</p>
      <div class="buy"><span class="price">$80</span><span class="book">Book Now</span></div>
    </div>
  </article>

  <article class="venue" style="left:256px;top:170px">
    <div class="pic pic-villa" role="img" aria-label="Photo of a modern villa with pool at twilight"><span>PRIME APPARTMENT</span></div>
    <div class="info">
      <div class="title"><span>Ut wisi enim</span><span>8/10</span></div>
      <p class="desc">Lorem ipsum dolor sit amet, consectetuer adipiscing elit, sed diam nonummy nibh euismod.</p>
      <div class="rate"><span class="stars"><svg width="40" height="7" viewBox="0 0 40 7"><g fill="#f2a623"><circle cx="3.5" cy="3.5" r="3"/><circle cx="11.5" cy="3.5" r="3"/><circle cx="19.5" cy="3.5" r="3"/></g><g fill="#ccc"><circle cx="27.5" cy="3.5" r="3"/><circle cx="35.5" cy="3.5" r="3"/></g></svg></span><span>More Info</span></div>
      <p class="per">Price per room per night from</p>
      <div class="buy"><span class="price">$80</span><span class="book">Book Now</span></div>
    </div>
  </article>
</section>

<section class="abs why">
  <h2>Why should you book your venue through <em>Pinevault</em>?</h2>

  <div class="reason" style="left:9px;top:52px"><h4>Handpicked Hotels</h4>Lorem ipsum dolor sit amet, consectetuer adipiscing elit, sed diam nonummy consectetuer adipiscing elit, nibh euismod.</div>
  <span class="reason-line" style="left:128px;top:50px"></span>
  <div class="reason" style="left:134px;top:52px"><h4>Detailed Descriptions</h4>Lorem ipsum dolor sit amet, consectetuer adipiscing elit, sed diam nonummy consectetuer adipiscing elit, nibh euismod.</div>
  <span class="reason-line" style="left:253px;top:50px"></span>
  <div class="reason" style="left:259px;top:52px"><h4>Exclusive Knowledge</h4>Lorem ipsum dolor sit amet, consectetuer adipiscing elit, sed diam nonummy consectetuer adipiscing elit, nibh euismod.</div>
  <span class="reason-line" style="left:378px;top:50px"></span>
  <div class="reason" style="left:384px;top:52px"><h4>Passionate Service</h4>Lorem ipsum dolor sit amet, consectetuer adipiscing elit, sed diam nonummy consectetuer adipiscing elit, nibh euismod.</div>

  <div class="reason" style="left:9px;top:142px"><h4>Best Price Guarantee</h4>Lorem ipsum dolor sit amet, consectetuer adipiscing elit, sed diam nonummy consectetuer adipiscing elit, nibh euismod.</div>
  <span class="reason-line" style="left:128px;top:140px"></span>
  <div class="reason" style="left:134px;top:142px"><h4>Secure Booking</h4>Lorem ipsum dolor sit amet, consectetuer adipiscing elit, sed diam nonummy consectetuer adipiscing elit, nibh euismod.</div>
  <span class="reason-line" style="left:253px;top:140px"></span>
  <div class="reason" style="left:259px;top:142px"><h4>Benefits for Hotellers</h4>Lorem ipsum dolor sit amet, consectetuer adipiscing elit, sed diam nonummy consectetuer adipiscing elit, nibh euismod.</div>
  <span class="reason-line" style="left:378px;top:140px"></span>
  <div class="reason" style="left:384px;top:142px"><h4>Any Questions ?</h4>Lorem ipsum dolor sit amet, consectetuer adipiscing elit, sed diam nonummy consectetuer adipiscing elit, nibh euismod.</div>
</section>

<footer class="abs footer">
  <div class="abs foot-brand"><span class="mark"></span><span>pinevault Bookings</span></div>
  <ul class="abs contact">
    <li><svg width="7" height="9" viewBox="0 0 8 10"><path d="M4 10S0 5.6 0 3.8a4 4 0 018 0C8 5.6 4 10 4 10z" fill="#444"/><circle cx="4" cy="3.8" r="1.4" fill="#eee"/></svg>12 Harbour Lane Millbrook VIC</li>
    <li><svg width="7" height="9" viewBox="0 0 8 10"><rect x="1" y="0" width="6" height="10" rx="1" fill="#444"/><rect x="2" y="1.5" width="4" height="6" fill="#eee"/></svg>03 5550 1427</li>
    <li><svg width="9" height="7" viewBox="0 0 10 7"><rect width="10" height="7" fill="#444"/><path d="M0 0l5 4 5-4" fill="none" stroke="#eee" stroke-width=".8"/></svg>info@bookings.pinevault.com.au</li>
  </ul>

  <div class="abs foot-col" style="left:235px;top:24px">Customer Support</div>
  <ul class="abs support-list">
    <li>• FAQs</li><li>• How do I make a reservation?</li><li>• Payment options</li><li>• Booking tips</li>
  </ul>

  <div class="abs foot-col" style="left:367px;top:22px">Follow us</div>
  <div class="abs social"><i class="on"></i><i></i><i></i><i></i><i></i><i></i><i></i><i></i></div>
  <div class="abs offers"><span>Our exclusive offers</span><span class="email">Enter your email here</span><span class="signup">SIGNUP</span></div>

  <div class="abs foot-nav">
    <ul><li>HOME</li><li>VENUE</li><li>NEWS &amp; OFFERS</li><li>INSPIRATION</li><li>SERVICES</li><li>CONTACT</li><li>FAQs</li></ul>
    <span class="copyright">© 2014, pinevault.com · All Rights Reserved.</span>
  </div>
</footer>

</body>
</html>
```